automatic Real Estate Sales Brochure

Print-out of 3 to 8 pages automatically on a color inkjet printer. Page size A4
All details for my Real Estate Sales Design Project are in attached file.
Here some points:
We have abound 100 real estate objects for sale (houses, flats and pieces of land).
For each item, our system creates automatically a sales documentation, which we print out and hand to the potential buyers after they've visited the object or send it by mail upon request in form of a pdf.
This document should be of 3 to maximum 8 pages.
It should be of a modern design and invite the client to read it.
The information should be clear and quick to find.
If the global look could somehow relate to the look of our web site www.velorancasa.ch, that would be nice.
The company data is there for legal reasons, but it is the agent's phone and mail that the clients should use for contact.
The photos should be of big size (2 by page?) without being distorted nor cut.
Optionally, to save ink and pages, maybe only the first 3-4 photos full size and the rest smaller?

Target Market(s)

will be printed or sent as PDF "on the fly", meaning no pre-printing at a print shop!

Industry/Entity Type

Real Estate

Font styles to use
Sans Serif

Requirements
Must have
• see details in attached file
Should not have
• no edge-to-edge printing
• no double-page printing (A3)

```html
<!DOCTYPE html>
<html lang="fr">
<head>
<meta charset="utf-8">
<title>Brochure de vente – VeloranCasa</title>
<link rel="stylesheet" href="https://fonts.googleapis.com/css2?family=Roboto+Condensed:wght@400;700&family=Lato:wght@400;700&display=swap">
<style>
:root{
  --red:#e30613;
  --ink:#3a3a3a;
  --dark:#4a4a4a;
  --paper:#f4f4f4;
  --paper-shade:#dedede;
  --stage:#e9e7e4;
  --floor:#b8692a;
  --wall:#efe9df;
}
*{box-sizing:border-box;margin:0;padding:0}
html,body{width:1200px;height:1200px;overflow:hidden;background:var(--stage)}
.canvas{position:relative;width:1200px;height:1200px;font-family:"Lato",sans-serif;color:var(--ink)}
.page{position:absolute;width:393px;height:552px;background:linear-gradient(135deg,#fff 0%,var(--paper) 55%,var(--paper-shade) 100%);overflow:hidden;box-shadow:0 2px 8px rgba(0,0,0,.18)}
.page svg.geo{position:absolute;inset:0;width:393px;height:552px}
.page-cover{left:114px;top:42px}
.page-details{left:729px;top:42px}
.page-gallery{left:422px;top:620px}
.bottom-bar{position:absolute;left:0;right:0;bottom:0;height:8px;background:var(--dark)}
.brand{position:absolute;display:flex;align-items:center;gap:5px;font-family:"Roboto Condensed",sans-serif;font-weight:700;color:var(--ink);letter-spacing:.2px}
.brand-mark{display:block;background:var(--red)}
.page-cover .brand{left:34px;top:40px;font-size:26px}
.page-cover .brand-mark{width:12px;height:12px}
.page-details .brand,.page-gallery .brand{left:20px;top:16px;font-size:19px}
.page-details .brand-mark,.page-gallery .brand-mark{width:9px;height:9px}

.cover-kicker{position:absolute;left:166px;top:410px;font-family:"Roboto Condensed",sans-serif;font-weight:700;font-size:10.5px;color:var(--ink)}
.cover-title{position:absolute;left:166px;top:422px;font-family:"Roboto Condensed",sans-serif;font-weight:700;font-size:31px;color:var(--red)}
.facts{position:absolute;top:484px;display:flex;gap:4px;font-family:"Roboto Condensed",sans-serif;font-size:7px;color:var(--ink)}
.facts-a{left:80px}.facts-b{left:231px}
.facts-labels{line-height:9px;padding-top:1px}
.facts-table{width:70px;border:1px solid #777;font-size:4.6px;text-align:right;background:#fff}
.facts-table div{padding:0 2px;line-height:7.4px;border-bottom:1px solid #ccc}
.facts-table div:first-child{background:#777;color:#fff}
.facts-table div:last-child{border-bottom:none}
.cover-url{position:absolute;left:0;width:290px;top:528px;text-align:center;font-size:7px;letter-spacing:2.6px;color:var(--red);font-weight:700}

.broker{position:absolute;right:16px;top:17px;text-align:right;font-size:6.5px;line-height:8px;color:#222}
.section-tab{position:absolute;left:0;height:13px;width:74px;background:var(--dark);color:#fff;font-size:7.5px;font-weight:700;padding:2px 0 0 18px;clip-path:polygon(0 0,100% 0,90% 100%,0 100%)}
.tab-description{top:84px}.tab-situation{top:262px}
.body-copy{position:absolute;left:18px;width:265px;font-size:4.9px;line-height:6.3px;color:#222}
.body-copy p{margin-bottom:6.5px}
.copy-description{top:101px}.copy-situation{top:284px}
.agent{position:absolute;left:293px;top:100px;width:60px;text-align:center}
.agent-photo{width:60px;height:80px;border:1px solid var(--red);background:linear-gradient(180deg,#d9d4cf,#6b5448 60%,#2a2624)}
.agent-name{font-size:7px;font-weight:700;margin-top:2px;color:#111}
.agent-contact{font-size:5.4px;line-height:6.6px;color:#222}

.tilt-photo{position:absolute;width:138px;height:138px;border:2px solid var(--red);transform:rotate(-35deg)}
.tilt-1{left:31px;top:369px;background:linear-gradient(180deg,var(--wall) 0%,#f7f3ea 50%,#c1833f 75%,var(--floor) 100%)}
.tilt-2{left:221px;top:367px;background:linear-gradient(180deg,#dcd9d4 0%,#f0eee9 50%,#a86a33 80%,#8a5424 100%)}

.gallery-photo{position:absolute;width:124px;height:116px;border:5px solid #5a5a5a;transform:rotate(-15deg)}
.g1{left:60px;top:70px;background:linear-gradient(180deg,#cfcbc6,#ece9e4 60%,#b9a58a)}
.g2{left:204px;top:18px;background:linear-gradient(150deg,#f3ecd9 0%,#2b2624 45%,#2b2624 60%,#c27d36 100%)}
.g3{left:67px;top:218px;background:linear-gradient(180deg,#e9e4da,#f5f2ea 55%,#c27f3a 80%,var(--floor))}
.g4{left:204px;top:170px;background:linear-gradient(180deg,#e6e2da,#f6f3ec 55%,#a86a33 85%)}
.g5{left:67px;top:378px;background:linear-gradient(180deg,#8fb7dd 0%,#6f9a45 40%,#3f6b26 100%)}
.g6{left:204px;top:330px;background:linear-gradient(180deg,#e4e4e2,#f2f2f0 60%,#cfcfcd)}

.contact-list{position:absolute;right:18px;top:465px;text-align:right;font-family:"Roboto Condensed",sans-serif;font-size:6.4px;color:#222;line-height:12.5px}
.contact-list li{list-style:none;display:flex;justify-content:flex-end;align-items:center;gap:4px}
.contact-list svg{width:7px;height:7px;fill:var(--red)}
.contact-list .company{line-height:7.8px;margin-top:2px;font-size:5.8px}
.page-gallery .bottom-bar{background:var(--red);height:4px}
</style>
</head>
<body>
<main class="canvas">

  <section class="page page-cover">
    <svg class="geo" viewBox="0 0 393 552">
      <defs>
        <linearGradient id="roomGrad" x1="0" y1="0" x2="0.3" y2="1">
          <stop offset="0" stop-color="#f4efe6"/>
          <stop offset="0.45" stop-color="#e7dfd2"/>
          <stop offset="0.62" stop-color="#c98a48"/>
          <stop offset="1" stop-color="#a85a22"/>
        </linearGradient>
      </defs>
      <polygon role="img" aria-label="Photo du séjour lumineux avec parquet et baies vitrées" points="0,150 34,136 393,34 393,400 250,316 0,540" fill="url(#roomGrad)"/>
      <polygon points="0,552 0,532 246,316 393,400 393,552" fill="#f6f6f6"/>
      <polyline points="0,98 34,122 393,10" fill="none" stroke="var(--red)" stroke-width="3"/>
      <polyline points="34,132 393,34" fill="none" stroke="var(--dark)" stroke-width="4"/>
      <polyline points="0,156 242,312 0,528" fill="none" stroke="var(--red)" stroke-width="6"/>
      <line x1="48" y1="140" x2="254" y2="312" stroke="var(--dark)" stroke-width="5"/>
      <line x1="250" y1="318" x2="393" y2="402" stroke="var(--dark)" stroke-width="4"/>
      <line x1="10" y1="552" x2="252" y2="326" stroke="var(--dark)" stroke-width="1.2"/>
    </svg>
    <div class="brand"><span class="brand-mark"></span>VeloranCasa</div>
    <p class="cover-kicker">LUMINEUX 4.5 DE 100M2 IDÉALEMENT SITUÉ !</p>
    <h1 class="cover-title">À 1200 GENÈVE</h1>
    <div class="facts facts-a">
      <div class="facts-labels">Type de bien<br>Surface habitable m2<br>Nombre de pièces<br>Surface parcelle m2</div>
      <div class="facts-table"><div>Appartement</div><div>100 m²</div><div>4,5</div><div>0 m²</div></div>
    </div>
    <div class="facts facts-b">
      <div class="facts-labels">Type de bien<br>Surface habitable m2<br>Nombre de pièces<br>Surface parcelle m2</div>
      <div class="facts-table"><div>Appartement</div><div>100 m²</div><div>4,5</div><div>0 m²</div></div>
    </div>
    <p class="cover-url">www.velorancasa.ch</p>
    <div class="bottom-bar"></div>
  </section>

  <section class="page page-details">
    <svg class="geo" viewBox="0 0 393 552">
      <polygon points="0,0 393,0 393,41 371,62 35,70 0,42" fill="#fff"/>
      <polyline points="159,0 371,62 393,41" fill="none" stroke="var(--red)" stroke-width="3"/>
      <polyline points="0,42 35,70 207,16" fill="none" stroke="var(--dark)" stroke-width="2"/>
    </svg>
    <div class="brand"><span class="brand-mark"></span>VeloranCasa</div>
    <div class="broker">Votre courtier<br>Nadia Rinaldi<br>0774802193</div>

    <div class="section-tab tab-description">Description</div>
    <div class="body-copy copy-description">
      <p>Venez visiter sans tarder ce bel appartement situé dans un environnement calme et vert tout en étant proche du centre-ville et de toutes les commodités. Il profite de beaux volumes et de pièces de vie très lumineuses. Au 1er étage d'une copropriété soignée, c'est le bien idéal pour un couple ou une famille.</p>
      <p>Cet appartement pourrait aussi convenir comme investissement pour un client souhaitant le louer.</p>
      <p>Il est en bon état d'entretien et se réjouit d'accueillir ses nouveaux propriétaires !</p>
      <p>Il se distribue ainsi :</p>
      <p>Une entrée avec armoire encastrée dessert de part et d'autre la partie jour et la partie nuit. La spacieuse pièce de vie se compose d'une cuisine ouverte entièrement équipée et aménagée s'ouvrant sur le séjour. Il profite d'une exposition optimale. Du séjour, vous avez accès à un agréable balcon qui offre une belle vue dégagée sur un environnement verdoyant.</p>
      <p>La partie nuit offre trois belles chambres, une salle de bains avec baignoire, lavabo, wc ainsi qu'un wc visiteurs.</p>
      <p>Deux places de parc intérieures en sus s'ajoutent à ce bel appartement !</p>
      <p style="margin-top:11px">N'hésitez pas, contactez-moi pour plus d'informations et pour une visite !</p>
    </div>

    <div class="agent">
      <div class="agent-photo" role="img" aria-label="Portrait de la courtière"></div>
      <div class="agent-name">NADIA RINALDI</div>
      <div class="agent-contact">rinaldi@velorancasa.ch<br>077 480 21 93</div>
    </div>

    <div class="section-tab tab-situation">Situation</div>
    <div class="body-copy copy-situation">
      <p>Cet appartement a l'avantage de se situer proche de toutes les commodités, à 3 minutes du Collège des Tilleuls, à 1 minute de l'arrêt de bus et à 3 minutes des axes autoroutiers. Vous rejoindrez le centre-ville en 7 minutes. Des atouts que vous saurez apprécier.</p>
    </div>

    <div class="tilt-photo tilt-1" role="img" aria-label="Photo du séjour d'angle avec baies vitrées"></div>
    <div class="tilt-photo tilt-2" role="img" aria-label="Photo du hall d'entrée avec portes"></div>
    <div class="bottom-bar"></div>
  </section>

  <section class="page page-gallery">
    <svg class="geo" viewBox="0 0 393 552">
      <polygon points="0,0 242,0 34,67 0,43" fill="#fff"/>
      <polyline points="0,43 34,67 242,0" fill="none" stroke="var(--red)" stroke-width="2.5"/>
      <line x1="0" y1="549" x2="393" y2="431" stroke="var(--red)" stroke-width="3"/>
      <line x1="70" y1="552" x2="393" y2="452" stroke="var(--red)" stroke-width="1.2"/>
    </svg>
    <div class="brand"><span class="brand-mark"></span>VeloranCasa</div>

    <div class="gallery-photo g1" role="img" aria-label="Photo de l'entrée avec armoires encastrées"></div>
    <div class="gallery-photo g2" role="img" aria-label="Photo d'une chambre avec armoire vitrée"></div>
    <div class="gallery-photo g3" role="img" aria-label="Photo d'une chambre avec fenêtre"></div>
    <div class="gallery-photo g4" role="img" aria-label="Photo d'une chambre lumineuse"></div>
    <div class="gallery-photo g5" role="img" aria-label="Photo du jardin arboré"></div>
    <div class="gallery-photo g6" role="img" aria-label="Photo de la salle d'eau"></div>

    <ul class="contact-list">
      <li>021 640 18 52 <svg viewBox="0 0 10 10"><path d="M2 1l2 0 1 2.5-1.3 1a5 5 0 0 0 2.8 2.8l1-1.3L10 7v2c0 .6-.4 1-1 1A9 9 0 0 1 0 1c0-.6.4-1 1-1z"/></svg></li>
      <li>021 640 18 50 <svg viewBox="0 0 10 10"><rect x="2" y="0" width="6" height="3"/><rect x="0" y="3.5" width="10" height="4" rx="1"/><rect x="2" y="7" width="6" height="3"/></svg></li>
      <li>021 640 18 50 info@velorancasa.ch <svg viewBox="0 0 10 10"><rect x="0" y="2" width="10" height="7"/><path d="M0 2l5 4 5-4" stroke="#fff" fill="none"/></svg></li>
      <li>www.velorancasa.ch <svg viewBox="0 0 10 10"><circle cx="5" cy="5" r="4.5" fill="none" stroke="#555" stroke-width="1"/><path d="M.5 5h9M5 .5v9" stroke="#555" stroke-width=".8"/></svg></li>
      <li class="company"><span>VeloranCasa Sàrl<br>Chemin des Vignes 7<br>1804 Corsier</span> <svg viewBox="0 0 10 10"><path d="M5 0a3.6 3.6 0 0 1 3.6 3.6C8.6 6.4 5 10 5 10S1.4 6.4 1.4 3.6A3.6 3.6 0 0 1 5 0z"/><circle cx="5" cy="3.6" r="1.3" fill="#fff"/></svg></li>
    </ul>
    <div class="bottom-bar"></div>
  </section>

</main>
</body>
</html>
```